We need an eye popping unique box for our electronic diffusers

We are a health and wellness company that is launching our new electronic diffuser. We are looking for something unique and eye catching for a box. This box will have extras in it so this is not a simple design. Also whatever design we pick will have potential for 6 more box designs of the same theme. We are looking for a "Zen", clean, natural, meditating kind of look. Namaste!
Updates

Target Market(s)

Mostly women but anyone really

Industry/Entity Type

Health And Wellness

Requirements
Must have
• Please read attached package document
• Must be unique and eye catching
• Must have 4 spots for essential oil bottles. Dimensions in file.
• Must keep to our logo for theme in some way so it looks harmonious
• Must be a "Zen", clean, nature, meditation like theme in some way, can deviate if it looks right
Should not have
• Nothing corporate looking

```html
<!DOCTYPE html>
<html lang="en">
<head>
<meta charset="utf-8">
<title>serenith Aroma Diffuser – Box Front</title>
<link rel="stylesheet" href="https://fonts.googleapis.com/css2?family=Jost:wght@300;400&display=swap">
<style>
  :root {
    --page-bg: #f4f5f7;
    --panel-black: #171717;
    --panel-deep: #101010;
    --smoke-light: rgba(150,150,150,0.30);
    --smoke-mid: rgba(110,110,110,0.28);
    --silver: #d6d6d8;
    --silver-soft: #c8c8ca;
  }
  html, body {
    margin: 0;
    padding: 0;
    width: 1117px;
    height: 1200px;
    overflow: hidden;
    background: var(--page-bg);
  }
  .canvas {
    position: relative;
    width: 1117px;
    height: 1200px;
  }
  .box-front {
    position: absolute;
    left: 241px;
    top: 60px;
    width: 635px;
    height: 1030px;
    background: var(--panel-black);
    overflow: hidden;
  }
  .smoke-art {
    position: absolute;
    inset: 0;
    background:
      radial-gradient(ellipse 28% 14% at 12% 34%, var(--smoke-light), transparent 70%),
      radial-gradient(ellipse 40% 10% at 38% 48%, var(--smoke-mid), transparent 70%),
      radial-gradient(ellipse 22% 20% at 88% 48%, var(--smoke-light), transparent 70%),
      radial-gradient(ellipse 35% 12% at 60% 58%, var(--smoke-mid), transparent 70%),
      radial-gradient(ellipse 30% 18% at 22% 66%, rgba(100,100,100,0.22), transparent 70%),
      radial-gradient(ellipse 26% 16% at 78% 74%, rgba(100,100,100,0.20), transparent 70%),
      radial-gradient(ellipse 30% 22% at 50% 15%, rgba(90,90,90,0.18), transparent 70%),
      linear-gradient(180deg, var(--panel-black), var(--panel-deep));
  }
  .brand-mark {
    position: absolute;
    left: 50%;
    top: 150px;
    width: 110px;
    height: 110px;
    margin-left: -55px;
    border-radius: 50%;
    background: var(--silver);
  }
  .brand-name {
    position: absolute;
    left: 0;
    right: 0;
    top: 300px;
    margin: 0;
    text-align: center;
    font-family: "Jost", sans-serif;
    font-weight: 300;
    font-size: 116px;
    letter-spacing: 0;
    line-height: 1;
    color: var(--silver);
  }
  .product-line {
    position: absolute;
    left: 0;
    right: 0;
    top: 830px;
    margin: 0;
    text-align: center;
    font-family: "Jost", sans-serif;
    font-weight: 400;
    font-size: 32px;
    letter-spacing: 0.5px;
    line-height: 1;
    color: var(--silver-soft);
  }
</style>
</head>
<body>
  <main class="canvas">
    <section class="box-front">
      <div class="smoke-art" role="img" aria-label="Soft wisps of grey smoke curling across a black background"></div>
      <span class="brand-mark" aria-hidden="true"></span>
      <h1 class="brand-name">serenith</h1>
      <p class="product-line">AROMA DIFFUSER</p>
    </section>
  </main>
</body>
</html>
```